Revamp of existing namecard

Existingly, i've got a namecard that i would like to retain the main design. but there are some changes in my company and i would need to do some amendments to it.

We are a money transfer and money exchange company.
I need 2 different types of name card.
1. For individual name cards
the front to put the following:
Company name and logo
English Name, Chinese Name appointment
Mobile Number, Email and Website.
2 License number under the logo and name

the back of the name card to put
8 address: 7 Singapore and 1 Hong Kong branch addresses
8 Mobile Number of the corresponding addresses.

We would like to retain the name card front design
the name card back design can change but color to retain.

2nd name card is generic name card
Front:
Company name and logo
Branch Mobile Number, Branch Address, Email and Website.

Industry/Entity Type

remittance and money exchange

Contact Information for Business Card

I need 2 different types of name card. 1. For individual name cards the front to put the following: Company name and logo English Name, Chinese Name appointment Mobile Number, Email and Website. 2 License number under the logo and name the back of the name card to put 8 address: 7 Singapore and 1 Hong Kong branch addresses 8 Mobile Number of the corresponding addresses. We would like to retain the name card front design the name card back design can change but color to retain. 2nd name card is generic name card Front: the front to put the following: Company name and logo Branch Mobile Number, Branch Address, Email and Website. 2 License number under the logo and name

Requirements
Must have
• I need 2 different types of name card. 1. For individual name cards the front to put the following: Company name and logo English Name, Chinese Name appointment Mobile Number, Email and Website. 2 License number under the logo and name the back of the name card to put 8 address: 7 Singapore and 1 Hong Kong branch addresses 8 Mobile Number of the corresponding addresses. We would like to retain the name card front design the name card back design can change but color to retain. 2nd name card is generic name card Front: the front to put the following: Company name and logo Branch Mobile Number, Branch Address, Email and Website. 2 License number under the logo and name
Nice to have
• use back color code

```html
<!DOCTYPE html>
<html lang="en">
<head>
<meta charset="utf-8">
<title>Talvorin name cards</title>
<link href="https://fonts.googleapis.com/css2?family=Montserrat:wght@400;500;600;700&family=Noto+Sans+TC:wght@500&family=Source+Sans+3:wght@400&display=swap" rel="stylesheet">
<style>
  :root{
    --bg:#e6e6e6;
    --ink:#2b3441;
    --navy:#2b3441;
    --navy-soft:#323c4a;
    --teal:#6fc6d6;
    --teal-faint:#d5eef2;
    --band:#5a8f9a;
    --white:#ffffff;
    --label:#111111;
  }
  *{margin:0;padding:0;box-sizing:border-box}
  html,body{width:1200px;height:858px;overflow:hidden;background:var(--bg)}
  .sheet{position:relative;width:1200px;height:858px;font-family:"Montserrat",sans-serif;color:var(--ink)}
  .section-label{position:absolute;left:149px;font-family:"Source Sans 3",sans-serif;font-size:25px;color:var(--label);font-weight:400}
  .section-label.individual{top:92px}
  .section-label.generic{top:469px}
  .card{position:absolute;width:394px;height:225px;box-shadow:4px 6px 8px rgba(0,0,0,.28);overflow:hidden}
  .card.front{left:136px;background:var(--white)}
  .card.back{left:648px;background:var(--navy)}
  .row-individual{top:157px}
  .row-generic{top:528px}
  .brand{position:absolute;display:flex;align-items:center;font-weight:600;letter-spacing:.2px;line-height:1}
  .brand-dot{border-radius:50%;background:var(--teal);flex:none}
  .front .brand{left:24px;top:24px;font-size:30px;gap:16px;color:var(--ink)}
  .front .brand-dot{width:28px;height:28px}
  .watermark{position:absolute;left:246px;top:97px;width:115px;height:115px;border-radius:50%;background:var(--teal-faint)}
  .person{position:absolute;left:24px}
  .person-name{font-size:19px;font-weight:700;line-height:1}
  .person-name-zh{font-family:"Noto Sans TC",sans-serif;font-size:16px;font-weight:500;color:var(--teal);line-height:1;margin-top:4px}
  .license{font-size:11px;font-weight:700;line-height:1}
  .contacts{position:absolute;left:24px;list-style:none;font-size:11.5px;font-weight:500;line-height:1}
  .contacts li{display:flex;align-items:flex-start;gap:4px}
  .contacts svg{flex:none;width:9px;height:11px}
  .individual-front .person{top:80px}
  .individual-front .license{position:absolute;left:24px;top:131px}
  .individual-front .contacts{top:158px}
  .individual-front .contacts li{margin-bottom:6.5px}
  .generic-front .person{top:71px}
  .generic-front .license{position:absolute;left:24px;top:96px}
  .generic-front .address{position:absolute;left:24px;top:118px;display:flex;gap:4px;font-size:11.5px;font-weight:500;line-height:15px}
  .generic-front .address svg{width:9px;height:11px;margin-top:2px;flex:none}
  .generic-front .contacts{top:163px}
  .generic-front .contacts li{margin-bottom:4px}
  .world-map{position:absolute;left:8px;top:18px;width:380px;height:190px;border-radius:40px;background:radial-gradient(ellipse at center,var(--navy-soft) 0%,var(--navy) 75%)}
  .back .brand{left:0;right:0;justify-content:center;color:var(--white)}
  .individual-back .brand{top:76px;font-size:30px;gap:8px}
  .individual-back .brand-dot{width:28px;height:28px}
  .generic-back .brand{top:88px;font-size:40px;gap:14px}
  .generic-back .brand-dot{width:36px;height:36px}
  .branch-band{position:absolute;left:0;top:154px;width:100%;height:41px;background:var(--band);color:var(--white);font-size:11.5px;font-weight:500;display:flex;align-items:center;justify-content:center}
</style>
</head>
<body>
<div class="sheet">

  <p class="section-label individual">individual name card:</p>

  <article class="card front individual-front row-individual">
    <div class="brand"><span class="brand-dot"></span>TALVORIN</div>
    <div class="person">
      <h2 class="person-name">Marcus Lee</h2>
      <p class="person-name-zh">李文軒</p>
    </div>
    <p class="license">License# 000000</p>
    <ul class="contacts">
      <li><svg viewBox="0 0 9 11"><rect x="1" y=".5" width="7" height="10" rx="1.2" fill="none" stroke="var(--teal)" stroke-width="1"/></svg>+852 5550 1234</li>
      <li><svg viewBox="0 0 9 11"><rect x="0" y="2.5" width="9" height="6" fill="var(--teal)"/><path d="M0 2.5 4.5 6 9 2.5" fill="none" stroke="#fff" stroke-width=".8"/></svg>marcus@talvorin.com.hk</li>
      <li><svg viewBox="0 0 9 11"><circle cx="4.5" cy="6" r="4" fill="none" stroke="var(--teal)" stroke-width=".9"/><path d="M.5 6h8M4.5 2v8" stroke="var(--teal)" stroke-width=".7"/></svg>www.talvorin.com.hk</li>
    </ul>
    <div class="watermark"></div>
  </article>

  <article class="card back individual-back row-individual">
    <div class="world-map" role="img" aria-label="Dotted world map background"></div>
    <div class="brand"><span class="brand-dot"></span>TALVORIN</div>
    <div class="branch-band">7 Singapore and 1 Hong Kong branch addresses</div>
  </article>

  <p class="section-label generic">generic name card:</p>

  <article class="card front generic-front row-generic">
    <div class="brand"><span class="brand-dot"></span>TALVORIN</div>
    <div class="person">
      <h2 class="person-name">Daniel Ross</h2>
    </div>
    <p class="license">License# 000000</p>
    <div class="address">
      <svg viewBox="0 0 9 11"><path d="M4.5 10.5C2 7 1 5.5 1 4a3.5 3.5 0 0 1 7 0c0 1.5-1 3-3.5 6.5z" fill="none" stroke="var(--teal)" stroke-width="1"/><circle cx="4.5" cy="4" r="1.2" fill="var(--teal)"/></svg>
      <p>7 Singapore and 1 Hong Kong<br>branch addresses</p>
    </div>
    <ul class="contacts">
      <li><svg viewBox="0 0 9 11"><rect x="1" y=".5" width="7" height="10" rx="1.2" fill="none" stroke="var(--teal)" stroke-width="1"/></svg>+852 5550 1234</li>
      <li><svg viewBox="0 0 9 11"><rect x="0" y="2.5" width="9" height="6" fill="var(--teal)"/><path d="M0 2.5 4.5 6 9 2.5" fill="none" stroke="#fff" stroke-width=".8"/></svg>marcus@talvorin.com.hk</li>
      <li><svg viewBox="0 0 9 11"><circle cx="4.5" cy="6" r="4" fill="none" stroke="var(--teal)" stroke-width=".9"/><path d="M.5 6h8M4.5 2v8" stroke="var(--teal)" stroke-width=".7"/></svg>www.talvorin.com.hk</li>
    </ul>
    <div class="watermark"></div>
  </article>

  <article class="card back generic-back row-generic">
    <div class="world-map" role="img" aria-label="Dotted world map background"></div>
    <div class="brand"><span class="brand-dot"></span>TALVORIN</div>
  </article>

</div>
</body>
</html>
```